Hartwell Falcons Soccer Club/Stepforward Football Programs needs a flyer for promotions to young students

We are a soccer(football) club based in Melbourne(suburb of Hartwell) and are running a professional 5 day a week all year round program for kids aged 8 to 18. Our target is to attract approximately 225 kids to our program by the 8th of march this year(4 weeks).
What sets our program apart is our message and mission statement:
- StepforwardFootball Programs will send players for a European or local Professional trial when they are ready
- Train like a professional 5 days a week all year round
- Proven program over 12 years
- Testimonials on website http://www.hartwellfalcons-qx.com
The message on the flyer needs to be clear and concise.
"Come and try our program FREE for 3 days"
Tom Brisley,Harbourvale Rovers 2015/2016 says "..............."
From only $10 a day
Norm Pellham Reserve cnr Tulley and Marsh Rd Hartwell
Positions Limited, Register Now.....website..............
Call Nilo Veta on 0400918273, Peter Manos on 0400736154, Andrew Paliris on 0400482690
Example of a flyer uploaded. Can we magnify our message?

Target Market(s)

children and youth aged 8 years to 18 years

Industry/Entity Type

Club

Requirements
Must have
• at least one testimonial
• background image
• clear, concise with no clutter

```html
<!DOCTYPE html>
<html lang="en">
<head>
<meta charset="utf-8">
<title>Hartwell Falcons Soccer Club – Stepforward Football Programs</title>
<link rel="stylesheet" href="https://fonts.googleapis.com/css2?family=Stardos+Stencil:wght@400;700&family=Alfa+Slab+One&family=Open+Sans:wght@400;600&family=Playfair+Display+SC:wght@900&display=swap">
<style>
  :root {
    --stage: #d9d9d9;
    --navy: #262c48;
    --dusk: #5b5a7a;
    --haze: #e9ece4;
    --cream: #f6f1e2;
    --sun: #f1dca6;
    --green: #3eaa3a;
    --green-bright: #4cc443;
    --frame-green: #7fe07a;
    --ink: #1e1e1e;
    --panel: #252525;
    --purple: #4a2fd0;
    --white: #ffffff;
  }
  * { box-sizing: border-box; margin: 0; padding: 0; }
  html, body { width: 1200px; height: 1200px; overflow: hidden; }
  body { background: var(--stage); position: relative; font-family: "Open Sans", Arial, sans-serif; }

  .flyer {
    position: absolute; left: 174px; top: 0; width: 852px; height: 1200px; overflow: hidden;
    background: linear-gradient(180deg, var(--navy) 0%, #3c4160 14%, var(--dusk) 28%, #a8a9b6 42%, var(--haze) 52%, #eef0ea 66%, var(--cream) 80%, var(--sun) 88%, var(--cream) 100%);
  }
  .club-name, .program-name {
    position: absolute; left: 0; width: 100%; text-align: center;
    font-family: "Stardos Stencil", "Georgia", serif; font-weight: 700; letter-spacing: 1px;
  }
  .club-name { top: 62px; font-size: 35px; color: var(--white); }
  .program-name { top: 110px; font-size: 38px; color: var(--green-bright); }

  .photo-strip {
    position: absolute; left: 62px; top: 192px; width: 722px; height: 370px;
    border: 4px solid var(--frame-green); background: var(--white);
    display: flex; gap: 7px;
  }
  .photo { height: 100%; }
  .photo-boot { width: 222px; background: linear-gradient(180deg, #0b0b0b 0%, #1a1a1a 55%, #3f7d2a 80%, #2f6a22 100%); }
  .photo-header { width: 236px; background: linear-gradient(180deg, #2f3338 0%, #6a7079 45%, #8fa07c 80%, #7fb64a 100%); }
  .photo-strike { flex: 1; background: linear-gradient(160deg, #2a1c40 0%, #6b3f78 40%, #8d6a56 75%, #9f8a3c 100%); }

  .testimonial { position: absolute; left: 0; top: 595px; width: 100%; text-align: center; color: var(--ink); }
  .testimonial-label { font-family: "Playfair Display SC", Georgia, serif; font-weight: 900; font-size: 18px; color: var(--purple); margin-bottom: 6px; }
  .testimonial p { font-size: 16.5px; line-height: 24px; }

  .offer {
    position: absolute; left: 37px; top: 682px; width: 778px; height: 130px;
    background: linear-gradient(180deg, #1d1d1d, var(--panel) 50%, #323232);
    border: 3px solid var(--green); border-radius: 26px;
    text-align: center; padding-top: 24px;
    font-family: "Stardos Stencil", Georgia, serif; font-weight: 700; font-size: 21.5px; line-height: 28.5px; letter-spacing: 1px; color: var(--white);
  }
  .offer .price { color: var(--green-bright); }

  .mission { position: absolute; left: 0; top: 848px; width: 100%; text-align: center; }
  .mission h2 { font-family: "Alfa Slab One", Georgia, serif; font-weight: 400; font-size: 16.5px; line-height: 22px; letter-spacing: 1px; color: var(--purple); }
  .mission p { font-size: 12.5px; line-height: 16px; color: var(--ink); margin-top: 3px; }

  .contact { position: absolute; left: 0; top: 974px; width: 100%; text-align: center; font-size: 15px; line-height: 19px; color: var(--ink); }

  .ball-glow {
    position: absolute; left: 30px; top: 992px; width: 104px; height: 104px; border-radius: 50%;
    background: radial-gradient(circle at 40% 35%, rgba(255,255,255,.7), rgba(230,205,140,.55) 60%, rgba(220,190,120,0) 100%);
  }

  .disclaimer-band { position: absolute; left: 0; top: 1076px; width: 100%; height: 78px; background: #1c1c1c; }
  .disclaimer-band svg { position: absolute; left: 0; top: 0; }
  .disclaimer-text {
    position: absolute; left: 0; top: 1090px; width: 100%; text-align: center;
    font-size: 14.5px; line-height: 18.5px; color: var(--white);
  }
</style>
</head>
<body>
  <main class="flyer">
    <h1 class="club-name">HARTWELL FALCONS SOCCER CLUB</h1>
    <div class="program-name">STEPFORWARDFOOTBALL PROGRAMS</div>

    <section class="photo-strip">
      <div class="photo photo-boot" role="img" aria-label="Close-up of a football boot resting on a ball on grass"></div>
      <div class="photo photo-header" role="img" aria-label="Two players leaping for a header in a floodlit stadium"></div>
      <div class="photo photo-strike" role="img" aria-label="Player in red kit striking a ball under stadium lights"></div>
    </section>

    <section class="testimonial">
      <div class="testimonial-label">Testimonial:</div>
      <p>"I WOULDN'T BE HERE WITHOUT YOU" TOM BRISLEY<br>PREMIER DIVISION, HARBOURVALE ROVERS SENIORS 2015</p>
    </section>

    <section class="offer">
      COME AND TRY OUR PROGRAM FREE FOR 3 DAYS"<br>
      TOM BRISLEY,HARBOURVALE ROVERS 2015/2016 SAYS "..............."<br>
      <span class="price">FROM ONLY $10 A DAY</span>
    </section>

    <section class="mission">
      <h2>MAKE YOUR SOCCER DREAM A REALITY<br>TRAIN LIKE THE PROFESSIONALS 5 DAYS A WEEK ALL YEAR ROUND</h2>
      <p>EUROPEAN AND LOCAL PROFESSIONAL TRIAL WHEN READY<br>"I WOULDN'T BE HERE WITHOUT YOU" TOM BRISLEY - PREMIER DIVISION, HARBOURVALE ROVERS SENIORS 2015</p>
    </section>

    <div class="ball-glow" role="img" aria-label="Faint soccer ball in warm light"></div>

    <section class="contact">
      Address: Norm Pellham Reserve, cnr Tulley st and Marsh rds Hartwell<br>
      Training times: 5pm-7pm Monday to Friday<br>
      Contact names and mobiles:<br>
      Nilo Veta 0400918273, Peter Manos&nbsp; 0400736154, Andrew Paliris&nbsp; 0400482690
    </section>

    <div class="disclaimer-band">
      <svg width="852" height="78" viewBox="0 0 852 78" aria-hidden="true">
        <polygon points="34,0 820,0 786,78 0,78" fill="var(--green)"/>
      </svg>
    </div>
    <p class="disclaimer-text">Disclaimer: only players that have completed the StepforwardFootball Program and deemed "ready", "complete"<br>by the coaching director will be eligible for European and local professional trials</p>
  </main>
</body>
</html>
```